Business Card Design Project

In addition to the logo design we want a professional and contemporary business card for a talent management agency. We provide management services to creative artists and want to communicate a professional creative vibe.
Updates

Reason: Sorry didnt realise I had put such a short timeline on it.

Target Market(s)

The business deals with creative artists and other industry professionals

Industry/Entity Type

Artists

Colors

Designer to choose colors to be used in the design.

Requirements
Must have
• Logo
Address
Phone
Email

```html
<!DOCTYPE html>
<html lang="en">
<head>
<meta charset="utf-8">
<title>Velo Artists — Business Card</title>
<link rel="stylesheet" href="https://fonts.googleapis.com/css2?family=Open+Sans:wght@400;700&display=swap">
<style>
  :root {
    --backdrop: #2b2b2c;
    --card: #0f0f10;
    --slate: #6c6c70;
    --mint: #5fa888;
    --silver: #a9a9ac;
    --ink-light: #ffffff;
    --ink-muted: #b9b9bc;
    --mark: #3a3a3d;
  }
  * { margin: 0; padding: 0; box-sizing: border-box; }
  html, body { width: 1200px; height: 1200px; overflow: hidden; }
  body {
    background: var(--backdrop);
    font-family: "Open Sans", Arial, sans-serif;
    position: relative;
  }
  .card {
    position: absolute;
    left: 300px;
    width: 600px;
    height: 340px;
    background: var(--card);
    border-radius: 6px;
    overflow: hidden;
  }
  .card--back { top: 150px; }
  .card--front { top: 560px; }
  .card__shapes { position: absolute; inset: 0; }
  .brand {
    position: absolute;
    right: 70px;
    bottom: 70px;
    color: var(--mark);
    font-weight: 700;
    line-height: 1;
    text-align: left;
  }
  .brand__name { font-size: 64px; letter-spacing: 2px; display: block; }
  .brand__sub { font-size: 28px; letter-spacing: 1px; display: block; margin-top: 6px; }
  .contact {
    position: absolute;
    right: 50px;
    top: 150px;
    text-align: right;
  }
  .contact__name { color: var(--ink-light); font-size: 26px; font-weight: 700; }
  .contact__line { color: var(--ink-muted); font-size: 13px; margin-top: 8px; }
  .contact__line:first-of-type { margin-top: 14px; }
  .spec {
    position: absolute;
    left: 97px;
    top: 1010px;
    display: flex;
    align-items: center;
    gap: 24px;
  }
  .spec__label { color: var(--ink-light); font-size: 15px; }
  .spec__swatches { display: flex; gap: 6px; }
  .swatch { width: 36px; height: 36px; }
  .swatch--mint { background: var(--mint); }
  .swatch--silver { background: var(--silver); }
</style>
</head>
<body>

  <section class="card card--back" aria-label="Card back">
    <svg class="card__shapes" viewBox="0 0 600 340" aria-hidden="true">
      <polygon points="0,0 0,150 170,0" fill="var(--slate)"/>
      <polygon points="170,0 0,150 0,230 300,0" fill="var(--mint)"/>
    </svg>
    <div class="brand">
      <span class="brand__name">VELO</span>
      <span class="brand__sub">Artists</span>
    </div>
  </section>

  <section class="card card--front" aria-label="Card front">
    <svg class="card__shapes" viewBox="0 0 600 340" aria-hidden="true">
      <polygon points="0,0 0,150 170,0" fill="var(--slate)"/>
      <polygon points="170,0 0,150 0,230 300,0" fill="var(--mint)"/>
    </svg>
    <div class="contact">
      <p class="contact__name">Mara Ellison</p>
      <p class="contact__line">8 Linden Street, Fitzroy VIC, Australia</p>
      <p class="contact__line">+61 3 9000 1234</p>
      <p class="contact__line">mara@veloartists.com</p>
    </div>
  </section>

  <div class="spec">
    <span class="spec__label">Embossed</span>
    <div class="spec__swatches">
      <span class="swatch swatch--mint"></span>
      <span class="swatch swatch--silver"></span>
    </div>
  </div>

</body>
</html>
```